Flyer Design for International Business Consultant

We need an advertisement to help build the profile of Miles Haversham, Senior Consultant and Director at 'ORB Advisory Group'.

What we want to promote:
Our Senior Consultant and Director, Miles Haversham as expert on all matters China related.

Who are we promoting to:
Industry associations and networking groups.

Why:
Many organisations are interested in reaching the Chinese market, however don't know who to go to or who to trust. With many consultants out there trying to claim they offer a similar service, ORB would like to promote Miles as a genuine expert in the field and the 'go to' person on all things China business related. To do this, we are in the process of building Miles's national and international profile, which includes advertising Miles expertise to industry associations and networking groups so that they consider booking Miles as a key note speaker at conferences. We know that our target audience are more inclined to seek the advice of someone they have seen speak at a conference than to find someone in the Golden listings or via findly search.

A Bit about Miles Haversham:

Miles Haversham has lived, worked and studied in China for extended periods, speaks and writes fluently in Chinese, was formerly a Member of the Tasmanian Government Trade Outreach Advisory Panel, is a member of the Institute of Global Commerce Studies and is a member of the Pacific Asia Enterprise Forum to name a few. To add to his credentials, Miles has by invitation lectured for 5 consecutive years in Management and Economics at Masters Level to students at Kowloon Harbour College.

Miles’s qualifications include: Bachelor of Arts (Asian Studies), Bachelor of Business (Applied Economics – International Trade), Master of Business in Applied Economics (International Business) and currently completing a Doctor of Business Administration (International Business Management) which has an economics focus and researches the export of Australian professional services to China.

Miles has been the Principal Consultant for a number of ORB’s clients including the recent assignment commissioned by Victorian based company BRN Freightways, who have benefited from a $40 million deal with Eastern Plains Locomotive (EPL). This project has also resulted in EPL, China’s largest train manufacturer decision to set up offices in Victoria.

Miles is an expert in Australia/China Business relations and has been paramount to the success of numerous international business transactions. As mentioned, Miles is not only fluent in spoken and written Mandarin, but is also a bi-cultural expert (meaning he knows both Australian and Chinese) cultures. From Australian and Chinese history, art, food and more, Miles Haversham provides his clients with more than translation services.

A Bit about ORB Advisory Group:

Run by experienced business executives with over 20 years’ experience in the Chinese and Australian markets, ORB brings a un-paralleled level of knowledge and expertise that enables cooperative business relations to develop between international organisations despite the language and cultural differences. They are a bi-lingual and bi-cultural international business consultancy that specialise in managing cross-border business involving China.

ORB has expertise in all facets of business management and has worked with a range of companies and organisations to develop and implement strategic business solutions to set direction, improve performance and maximise returns to stakeholders. ORB has particular expertise in economic and market analysis and specialises in project management of large and complex projects, strategic procurement, market research and market development strategies. Combined with their cultural and language skills, ORB provides a unique and high value contribution to international projects.

Good afternoon designers

Thank you for your submissions so far.  We are happy with some of the designs that have come in, however, many of you have produced flyers that have too much information in it.  We are looking for something more concise that does not appear to be either a copy of information I have posted in this brief or a fancy looking resume for Miles Haversham. 

Please remember, we are communicating to event co-ordinators who are looking to appoint guest speakers at an upcoming conference.  They want someone who is going to discuss some of the 'hot topics' their audience are interested in, someone who is experienced in the topic and someone who is interesting. We need to communicate all of this in a concise, and creative way so that we can make Miles Haversham stand out above the rest.

Dear Designers

Thank you all very much for your submissions.  We appreciate you taking the time to compose a flyer for our organisation. 

Regards
Rosa

Dear Designers

Regards
Rosa

Target Market(s)

Event/conference managers or coordinators

Industry/Entity Type

Business Management

Requirements
Must have
• Must have the ORB Logo on it (red, white and black). The ad will be in the form of an electronic flyer to be embedded in an email that will be sent on to relevant contacts in our database.

```html
<!DOCTYPE html>
<html lang="en">
<head>
<meta charset="utf-8">
<title>Miles Haversham – ORB Advisory Group</title>
<link rel="stylesheet" href="https://fonts.googleapis.com/css2?family=Open+Sans:wght@400;600;700&display=swap">
<style>
  :root {
    --page-bg: #d6d6d6;
    --card-bg: #ffffff;
    --brand-red: #c8161d;
    --deep-red: #6e0b10;
    --header-red-top: #8a0f15;
    --header-red-bottom: #5a070b;
    --title-red: #ff4a4a;
    --ink: #1c1c1c;
    --body-ink: #2a2a2a;
    --rule: #6e0b10;
  }
  * { box-sizing: border-box; margin: 0; padding: 0; }
  html, body { width: 848px; height: 1200px; overflow: hidden; }
  body {
    background: var(--page-bg);
    font-family: "Open Sans", Arial, sans-serif;
    color: var(--body-ink);
    position: relative;
  }
  .card {
    position: absolute;
    left: 14px;
    width: 820px;
    background: var(--card-bg);
    border-radius: 14px;
    overflow: hidden;
  }

  /* Intro card */
  .intro { top: 21px; height: 285px; }
  .intro-header {
    height: 67px;
    background: linear-gradient(var(--header-red-top), var(--header-red-bottom));
    display: flex;
    align-items: flex-end;
    justify-content: flex-end;
    padding: 0 30px 12px 0;
    gap: 16px;
  }
  .role-title { color: var(--title-red); font-size: 19px; font-weight: 400; line-height: 1; padding-bottom: 2px; }
  .speaker-name { color: #fff; font-size: 30px; font-weight: 400; line-height: 1; }

  .brand {
    position: absolute;
    left: 33px;
    top: 150px;
    display: flex;
    align-items: center;
    gap: 16px;
  }
  .brand-mark {
    width: 52px; height: 52px;
    border-radius: 50%;
    background: var(--brand-red);
    flex: none;
  }
  .brand-name {
    color: var(--ink);
    font-size: 34px;
    font-weight: 700;
    line-height: 1;
    white-space: nowrap;
  }

  .intro-copy {
    position: absolute;
    left: 510px;
    top: 117px;
    width: 270px;
    font-size: 9.3px;
    line-height: 14px;
  }

  /* Imagery card */
  .imagery { top: 321px; height: 342px; }
  .imagery svg { position: absolute; left: 24px; top: 21px; }

  /* Story card */
  .story { top: 677px; height: 494px; padding: 16px 33px 0 33px; }
  .story h2 { color: var(--brand-red); font-size: 22px; font-weight: 400; line-height: 1; margin-bottom: 11px; }
  .story p { font-size: 9.3px; line-height: 14.2px; }
  .rule { height: 2px; background: var(--rule); margin: 16px 10px 16px 0; }
  .profile p { line-height: 15.2px; }
  .closing p { color: var(--brand-red); font-size: 12px; line-height: 16px; }
</style>
</head>
<body>

<section class="card intro">
  <header class="intro-header">
    <span class="role-title">Senior Consultant and Director</span>
    <span class="speaker-name">Miles Haversham</span>
  </header>
  <div class="brand">
    <div class="brand-mark"></div>
    <div class="brand-name">ORB Advisory Group</div>
  </div>
  <p class="intro-copy">Run by experienced business executives with over 20 years’ experience in the Chinese and Australian markets, ORB brings a un-paralleled level of knowledge and expertise that enables cooperative business relations to develop between international organisations despite the language and cultural differences. They are a bi-lingual and bi-cultural international business consultancy that specialise in managing cross-border business involving China.</p>
</section>

<section class="card imagery">
  <svg width="770" height="296" viewBox="0 0 770 296">
    <defs>
      <linearGradient id="city-night" x1="0" y1="0" x2="0" y2="1">
        <stop offset="0" stop-color="#1d2f6b"/>
        <stop offset="0.45" stop-color="#3c4f8f"/>
        <stop offset="0.7" stop-color="#6b4a3a"/>
        <stop offset="1" stop-color="#c07a3a"/>
      </linearGradient>
      <linearGradient id="tower-mono" x1="0" y1="0" x2="1" y2="1">
        <stop offset="0" stop-color="#f2f2f2"/>
        <stop offset="0.5" stop-color="#6a6a6a"/>
        <stop offset="1" stop-color="#151515"/>
      </linearGradient>
    </defs>
    <rect role="img" aria-label="City skyline at dusk with lit streets below" x="0" y="0" width="472" height="296" fill="url(#city-night)"/>
    <rect role="img" aria-label="Black and white view looking up at glass office towers" x="472" y="0" width="298" height="296" fill="url(#tower-mono)"/>
  </svg>
</section>

<section class="card story">
  <h2>Industry associations and networking groups.</h2>
  <p>Many organisations are interested in reaching the Chinese market, however don’t know who to go to or who to trust. With many consultants out there trying to claim they offer a similar service, ORB would like to promote Miles as a genuine expert in the field and the ‘go to’ person on all thing China business related. To do this, we are in the process of building Miles’s national and international profile, which includes advertising Miles expertise to industry associations and networking groups so that they consider booking Miles as a key note speaker at conferences. We know that our target audience are more inclined to seek the advice of someone they have seen speak at a conference than to find someone in the Golden listings or via findly search.</p>

  <div class="rule"></div>

  <div class="profile">
    <p>Miles Haversham has lived, worked and studied in China for extended periods, speaks and writes fluently in Chinese, was formerly a Member of the Tasmanian Government Trade Outreach Advisory Panel, is a member of the Institute of Global Commerce Studies and is a member of the Pacific Asia Enterprise Forum to name a few.</p>
    <p>To add to his credentials, Miles has by invitation lectured for 5 consecutive years in Management and Economics at Masters Level to students at Kowloon Harbour College.</p>
    <p>Miles’s qualifications include: Bachelor of Arts (Asian Studies), Bachelor of Business (Applied Economics – International Trade), Master of Business in Applied Economics (International Business) and currently completing a Doctor of Business Administration (International Business Management) which has an economics focus and researches the export of Australian professional services to China.</p>
    <p>Miles has been the Principal Consultant for a number of ORB’s clients including the recent assignment commissioned by Victorian based company BRN Freightways, who have benefited from a $40 million deal with Eastern Plains Locomotive (EPL). This project has also resulted in EPL, China’s largest train manufacturer decision to set up offices in Victoria.</p>
    <p>Miles is an expert in Australia/China Business relations and has been paramount to the success of numerous international business transactions. As mentioned, Miles is not only fluent in spoken and written Mandarin, but is also a bi-cultural expert (meaning he knows both Australian and Chinese) cultures. From Australian and Chinese history, art, food and more, Miles Haversham provides his clients with more than translation services.</p>
  </div>

  <div class="rule"></div>

  <div class="closing">
    <p>ORB has expertise in all facets of business management and has worked with a range of companies and organisations to develop and implement strategic business solutions to set direction, improve performance and maximise returns to stakeholders. ORB has particular expertise in economic and market analysis and specialises in project management of large and complex projects, strategic procurement, market research and market development strategies. Combined with their cultural and language skills, ORB provides a unique and high value contribution to international projects.</p>
  </div>
</section>

</body>
</html>
```